Flyer-Design für Dienst für professionelle Fahrzeugpflege
Zielgruppe
Dienst für professionelle Fahrzeugpflege, Nano- Keramikversiegelung, 3-Stufen Politur, Hol- und Bringdienst Autowäsche, Politur, Innenraumreinigung, Geruchsentfernung, Flecken entfernen auf den Sitzen / Polster
Autoliebhaber, junge Leute, Geschäftsführer, Firmen, Leute die Ihr auto nicht mehr alleine Waschen können/möchten
Aufgabenstellung
Das Design sollte sehr Edel aber zugleich sportlich aussehen. Es sollte die junge Zielgruppe sowie den erfolgreichen Geschäftsführer ansprechen.

```html
<!DOCTYPE html>
<html lang="de">
<head>
<meta charset="utf-8">
<title>ShineWerk – Flyer Fahrzeugpflege</title>
<link href="https://fonts.googleapis.com/css2?family=Montserrat:wght@400;500;600;700;800&display=swap" rel="stylesheet">
<style>
  :root {
    --bg: #e9e4e1;
    --black: #070707;
    --red: #d2181f;
    --white: #ffffff;
    --grey: #cfcfcf;
  }
  * { margin: 0; padding: 0; box-sizing: border-box; }
  html, body { width: 1200px; height: 750px; overflow: hidden; background: var(--bg); }
  body { font-family: 'Montserrat', sans-serif; position: relative; }

  .flyer {
    position: absolute; left: 352px; top: 25px;
    width: 495px; height: 700px;
    background: var(--black);
    overflow: hidden;
    box-shadow: 0 8px 28px rgba(0,0,0,.25);
  }
  .hero-photo {
    position: absolute; left: 0; top: 0; width: 100%; height: 430px;
    background:
      linear-gradient(180deg, rgba(7,7,7,0) 70%, rgba(7,7,7,.75) 100%),
      linear-gradient(150deg,
        #9b9a95 0%, #6e6d69 14%,
        #b8342a 26%, #e4604c 40%, #d63a2c 52%,
        #a8201a 64%, #6b1512 74%,
        #3c3c3a 86%, #555553 100%);
  }
  .headline-box {
    position: absolute; left: 38px; top: 318px; width: 300px; height: 78px;
    background: linear-gradient(90deg, rgba(40,6,7,.94), rgba(90,12,14,.86));
    padding: 14px 0 0 26px;
    color: var(--white); text-transform: uppercase;
  }
  .headline-light { font-weight: 400; font-size: 21px; letter-spacing: 1px; line-height: 1.1; }
  .headline-bold { font-weight: 800; font-size: 23px; letter-spacing: .5px; line-height: 1.15; }
  .cta-band {
    position: absolute; left: 38px; top: 396px; right: 0; height: 34px;
    background: var(--red); color: var(--white);
    font-size: 10.5px; font-weight: 500; letter-spacing: 3.6px;
    display: flex; align-items: center; padding-left: 26px; text-transform: uppercase;
    white-space: nowrap;
  }
  .cta-band .url { text-transform: none; letter-spacing: 3px; }
  .services {
    position: absolute; left: 64px; top: 468px; list-style: none;
    color: var(--white); text-transform: uppercase;
    font-size: 15.5px; font-weight: 600; letter-spacing: .6px;
  }
  .services li { display: flex; align-items: center; gap: 8px; height: 30px; white-space: nowrap; }
  .services svg { width: 18px; height: 14px; }
  .brand {
    position: absolute; right: 28px; top: 478px; width: 110px;
    display: flex; flex-direction: column; align-items: center; gap: 8px;
    color: var(--white); font-weight: 700; font-size: 15px; letter-spacing: .5px; text-transform: uppercase;
  }
  .brand-dot { width: 34px; height: 34px; border-radius: 50%; background: var(--white); }
  .divider { position: absolute; left: 64px; top: 600px; width: 360px; height: 2px; background: var(--red); }
  .contact {
    position: absolute; top: 616px; color: var(--grey);
    font-size: 10px; line-height: 1.35; font-weight: 500; font-style: normal;
  }
  .contact.address { left: 64px; }
  .contact.reach { left: 270px; }
</style>
</head>
<body>
  <main class="flyer">
    <div class="hero-photo" role="img" aria-label="Foto eines mattroten Sportwagens in einer Werkstatt, Frontansicht mit Scheinwerfer und Felge"></div>

    <div class="headline-box">
      <p class="headline-light">Professionelle</p>
      <p class="headline-bold">Fahrzeugpflege</p>
    </div>
    <div class="cta-band">Jetzt informieren&nbsp;|&nbsp;<span class="url">www.shinewerk-pflege.de</span></div>

    <ul class="services">
      <li>Nano Keramikversiegelung <svg viewBox="0 0 18 14"><path d="M2 7l5 5L16 2" fill="none" stroke="#d2181f" stroke-width="2.4"/></svg></li>
      <li>3 - Stufen Politur <svg viewBox="0 0 18 14"><path d="M2 7l5 5L16 2" fill="none" stroke="#d2181f" stroke-width="2.4"/></svg></li>
      <li>Hol- und Bringservice <svg viewBox="0 0 18 14"><path d="M2 7l5 5L16 2" fill="none" stroke="#d2181f" stroke-width="2.4"/></svg></li>
      <li>Umfassende Innenraumreinigung <svg viewBox="0 0 18 14"><path d="M2 7l5 5L16 2" fill="none" stroke="#d2181f" stroke-width="2.4"/></svg></li>
    </ul>

    <div class="brand">
      <span class="brand-dot"></span>
      <span class="brand-name">ShineWerk</span>
    </div>

    <div class="divider"></div>
    <address class="contact address">ShineWerk<br>Lindenweg 12,<br>79000 Musterstadt, Deutschland</address>
    <p class="contact reach">Tel.: 0152/00047113<br>E-Mail: kontakt@shinewerk-pflege.de</p>
  </main>
</body>
</html>
```